BrightLoop Kiosk Business Card Design Project

BrightLoop Kiosk requires a business card design. We hire PhotoBooths to events such as Birthday Parties, Hens and Bucks Night, Anniversaries, Corporate Functions
, Engagements, Theme Nights, Presentation Night etc.
Business Card needs to look Modern, Professional And Catchy.
Updates

Hello Thankyou for all of your great designs, contact information will be provided shortly. We are considering the front of the card to be white themed and the back of the card to be black themed. And all social media colours to be their original colour. Thankyou

Hello everyone, Here are the contact details: Martin Colby - Manager Mobile number - 0491738205 Website - www.brightloopkiosk.example Email - admin@brightloopkiosk.example And if you can add the word "weddings" in the "We cater For" section would be good. Thankyou

Target Market(s)

Birthday Parties
Hens and Bucks Night
Weddings
Corporate Functions
Engagements
Theme Nights
Presentation Night
School Functions

Industry/Entity Type

Events

Requirements
Must have
• Must Match Logo
Must Have www.brightloopkiosk.example

On Back of card must have social media icons Facebook, Twitter, Youtube, Linkin and

We Cater For:

Birthday Parties
Hens and Bucks Night
Anniversaries
Corporate Functions
Engagements
Theme Nights
Presentation Night
School Functions
And more.....

```html
<!DOCTYPE html>
<html lang="en">
<head>
<meta charset="utf-8">
<title>BrightLoop Kiosk Business Card</title>
<link rel="stylesheet" href="https://fonts.googleapis.com/css2?family=Open+Sans:wght@400;600;700&display=swap">
<style>
  :root {
    --backdrop: #eceff1;
    --card-light: #26cdf2;
    --card-mid: #12b3ec;
    --card-deep: #0a86dc;
    --ink: #27343d;
    --ink-soft: #33434e;
    --name: #6a2f2f;
    --white: #ffffff;
  }
  * { box-sizing: border-box; margin: 0; padding: 0; }
  html, body {
    width: 1200px; height: 913px; overflow: hidden;
    background: var(--backdrop);
    font-family: "Open Sans", Arial, sans-serif;
    color: var(--ink);
  }
  .canvas {
    position: relative; width: 1200px; height: 913px;
    display: flex; align-items: center; justify-content: center; gap: 40px;
  }
  .card {
    position: relative; width: 560px; height: 320px; border-radius: 4px;
    background: linear-gradient(200deg, var(--card-light) 0%, var(--card-mid) 50%, var(--card-deep) 100%);
    box-shadow: 0 6px 18px rgba(0,0,0,0.18);
    overflow: hidden;
  }
  .brand {
    position: absolute; display: flex; align-items: center; gap: 14px;
    font-weight: 700; color: var(--ink); letter-spacing: 1px;
  }
  .brand-mark { width: 30px; height: 30px; background: var(--ink); flex: none; }
  .card-back .brand { left: 110px; top: 58px; font-size: 34px; }
  .cater-title {
    position: absolute; left: 0; right: 0; top: 138px; text-align: center;
    font-size: 15px; color: var(--ink-soft);
  }
  .cater-list {
    position: absolute; left: 0; right: 0; top: 164px; list-style: none;
    text-align: center; font-size: 16px; line-height: 24px; color: var(--ink-soft);
  }
  .cater-list span { margin: 0 6px; }
  .social-row {
    position: absolute; left: 0; right: 0; top: 262px;
    display: flex; justify-content: center; gap: 12px;
  }
  .social-tile { width: 22px; height: 22px; background: var(--white); }
  .card-front .brand { left: 40px; top: 214px; font-size: 30px; }
  .person { position: absolute; left: 300px; top: 62px; }
  .person-name { font-size: 17px; font-weight: 700; color: var(--name); }
  .person-role { font-size: 11px; color: var(--ink-soft); }
  .contact-list {
    position: absolute; left: 300px; top: 130px; list-style: none;
    font-size: 13px; color: var(--white); line-height: 22px;
  }
  .contact-list li { display: flex; align-items: center; gap: 8px; }
  .contact-list svg { width: 12px; height: 12px; fill: var(--ink); flex: none; }
</style>
</head>
<body>
<main class="canvas">
  <section class="card card-back">
    <div class="brand"><span class="brand-mark"></span>BrightLoop Kiosk</div>
    <p class="cater-title">We Cater For:</p>
    <ul class="cater-list">
      <li><span>» Birthday Parties</span><span>» Hens and Bucks Night</span><span>» Anniversaries</span></li>
      <li><span>» Corporate Functions</span><span>» Engagements</span><span>» Theme Nights</span></li>
      <li><span>» Presentation Night</span><span>» School Functions</span><span>» And more.....</span></li>
    </ul>
    <div class="social-row">
      <span class="social-tile"></span><span class="social-tile"></span>
      <span class="social-tile"></span><span class="social-tile"></span>
    </div>
  </section>

  <section class="card card-front">
    <div class="person">
      <p class="person-name">Your Long Name</p>
      <p class="person-role">Managing Director</p>
    </div>
    <ul class="contact-list">
      <li><svg viewBox="0 0 12 12"><path d="M6 0a4 4 0 0 1 4 4c0 3-4 8-4 8S2 7 2 4a4 4 0 0 1 4-4zm0 2.5a1.5 1.5 0 1 0 0 3 1.5 1.5 0 0 0 0-3z"/></svg>Your Commercial or office address</li>
      <li><svg viewBox="0 0 12 12"><path d="M1 4c0-2 2-3 5-3s5 1 5 3l-2 1-1-1.5H4L3 5zM3 6h6l1 5H2z"/></svg>00.00.00.0000 &nbsp; 00.00.00.0000</li>
      <li><svg viewBox="0 0 12 12"><path d="M0 2h12v8H0zm1 1v.5l5 3.5 5-3.5V3z"/></svg>yourname@yourwebsite.com</li>
      <li><svg viewBox="0 0 12 12"><circle cx="6" cy="6" r="5.5"/></svg>www.brightloopkiosk.example</li>
    </ul>
    <div class="brand"><span class="brand-mark"></span>BrightLoop Kiosk</div>
  </section>
</main>
</body>
</html>
```